Service Menu refresh 2018 Update of menu pricing

We currently have service menus as attached. We will be updating our look via our homepage image, our service menu and our in-house beverage and treatment menu.
We are a natural and sustainable hair salon group and moving more towards head spa which consists of treatments, beauty, tanning as well as your traditional hair services. Our imagery needs to reflect our efforts in spa treatments in the hair and scalp area and use natural materials and colours reflecting sustainability.
Elvu is the brand we stock and promote.

Target Market(s)

Men or women interesting in personal maintenance with natural and organic products and using sustainable practises

Industry/Entity Type

Hair And Beauty

Font styles to use
Sans Serif
Other font styles liked:
• Arial or Helvetica

Colors
9acb3c
abd037
cadf82
ffffff

Requirements
Must have
• Name on the front cover, locations on back cover
Nice to have
• Prestige feel, reflect male and female clients
Should not have
• Bold artificial writing or any type of cartoon images.
• Same images as existing menu.

```html
<!DOCTYPE html>
<html lang="en">
<head>
<meta charset="utf-8">
<title>Salon Service Menu</title>
<link rel="stylesheet" href="https://fonts.googleapis.com/css2?family=Montserrat:ital,wght@0,300;0,400;0,500;0,600;0,700;1,400;1,600;1,700;1,800&display=swap">
<style>
  :root {
    --green: #9acb3c;
    --green-2: #abd037;
    --green-light: #cadf82;
    --white: #ffffff;
    --yellow: #f6dc45;
    --ink: #4a4a4a;
    --ink-soft: #5e5e5e;
    --backdrop: #c9e083;
    --paper: #f7f8f3;
  }
  * { box-sizing: border-box; margin: 0; padding: 0; }
  html, body { width: 1200px; height: 1200px; overflow: hidden; background: var(--backdrop); }
  .menu-page {
    position: absolute; left: 171px; top: 0; width: 858px; height: 1200px;
    background: var(--paper); overflow: hidden;
    font-family: "Montserrat", Arial, sans-serif; color: var(--ink);
  }
  .hero-photo {
    position: absolute; left: 0; top: 0; width: 858px; height: 283px;
    background: linear-gradient(120deg, #1d2420 0%, #4f5b55 35%, #7a6a5a 60%, #3a3530 85%, #8a7e6a 100%);
  }
  .value-tabs { position: absolute; top: 230px; left: 63px; display: flex; }
  .value-tab { width: 183px; height: 53px; display: flex; align-items: center; justify-content: center;
    color: var(--white); font-size: 17px; letter-spacing: 1.5px; font-weight: 500; }
  .value-tab.t1 { background: rgba(202,223,130,.25); }
  .value-tab.t2 { background: rgba(171,208,55,.25); }
  .value-tab.t3 { background: rgba(154,203,60,.25); }
  .value-tab.t4 { background: rgba(246,220,69,.15); }
  .value-bands { position: absolute; top: 283px; left: 63px; display: flex; }
  .value-bands span { width: 183px; height: 24px; }
  .value-bands .b1 { background: linear-gradient(90deg, var(--green-2), var(--green-light)); }
  .value-bands .b2 { background: var(--green-light); }
  .value-bands .b3 { background: var(--green); }
  .value-bands .b4 { background: var(--yellow); }

  .section-title { position: absolute; font-family: "Montserrat", Arial, sans-serif; font-style: italic;
    font-weight: 700; font-size: 33px; color: var(--ink); letter-spacing: 0.5px; white-space: nowrap; line-height: 60px; }
  .section-title .brace { color: var(--green); font-weight: 300; font-size: 50px; vertical-align: -3px; font-style: normal; }

  .size-badge { position: absolute; width: 46px; height: 46px; }
  .size-badge b { position: absolute; inset: 0; display: flex; align-items: center; justify-content: center;
    font-style: italic; font-weight: 700; font-size: 17px; color: var(--ink); padding-top: 6px; }

  .row { position: absolute; left: 80px; width: 334px; font-size: 15.5px; white-space: nowrap; overflow: hidden; }
  .row.item { font-style: italic; color: var(--ink-soft); }
  .row.cat { font-weight: 500; letter-spacing: 1.3px; }
  .row.lead::after { content: " ........................................................................................"; letter-spacing: 1px; }
  .price { position: absolute; font-size: 15.5px; font-weight: 600; transform: translateX(-50%); }

  .foliage { position: absolute; left: 600px; top: 478px; width: 200px; height: 190px; border-radius: 14px;
    background: linear-gradient(135deg, rgba(154,203,60,.18), rgba(202,223,130,.12)); }
  .photo-circle { position: absolute; border-radius: 50%; border: 5px solid var(--yellow); }
  .photo-circle.one { left: 573px; top: 498px; width: 128px; height: 128px; background: linear-gradient(135deg, #c79a82, #e9d6c8 60%, #8a6a58); }
  .photo-circle.two { left: 668px; top: 536px; width: 128px; height: 128px; background: linear-gradient(135deg, #9fc3d3, #f1ebe6 55%, #cfa990); }

  .price-box { position: absolute; top: 878px; width: 163px; height: 58px; background: var(--green-light);
    font-style: italic; font-size: 15px; color: var(--ink-soft); padding: 19px 0 0 15px; white-space: nowrap; }
  .price-tag { position: absolute; width: 44px; height: 44px; right: -1px; bottom: -22px; }
  .price-tag b { position: absolute; inset: 0; display: flex; align-items: center; justify-content: center;
    font-weight: 700; font-style: italic; font-size: 13px; color: var(--ink); padding-top: 6px; }

  .footnote { position: absolute; left: 459px; top: 984px; width: 345px;
    font-style: italic; font-weight: 600; font-size: 10.5px; line-height: 15px; color: var(--ink); }
  .spa-photo { position: absolute; left: 0; top: 955px; width: 858px; height: 245px;
    background: linear-gradient(180deg, rgba(247,248,243,0) 0%, rgba(232,205,185,.7) 45%, #d8b49b 100%); }
</style>
</head>
<body>
<main class="menu-page">
  <div class="hero-photo" role="img" aria-label="Stylist cutting long brown hair with comb and scissors"></div>
  <div class="value-tabs">
    <div class="value-tab t1">BEAUTIFUL</div>
    <div class="value-tab t2">NATURAL</div>
    <div class="value-tab t3">HEALTHY</div>
    <div class="value-tab t4">ORGANIC</div>
  </div>
  <div class="value-bands"><span class="b1"></span><span class="b2"></span><span class="b3"></span><span class="b4"></span></div>

  <h2 class="section-title" style="left:58px;top:336px;"><span class="brace">{</span>CUT &amp; BLOWDRY<span class="brace">}</span></h2>

  <svg width="0" height="0" style="position:absolute">
    <defs>
      <symbol id="badge" viewBox="0 0 46 46">
        <circle cx="23" cy="23" r="22" fill="#f6dc45"/>
        <path d="M6 20 C10 6 26 0 44 2 C40 14 28 24 6 20 Z" fill="#7fb832"/>
      </symbol>
    </defs>
  </svg>
  <div class="size-badge" style="left:486px;top:359px;"><svg width="46" height="46"><use href="#badge"/></svg><b>S</b></div>
  <div class="size-badge" style="left:574px;top:359px;"><svg width="46" height="46"><use href="#badge"/></svg><b>M</b></div>
  <div class="size-badge" style="left:663px;top:359px;"><svg width="46" height="46"><use href="#badge"/></svg><b>L</b></div>
  <div class="size-badge" style="left:752px;top:359px;"><svg width="46" height="46"><use href="#badge"/></svg><b>XL</b></div>

  <div class="row cat lead" style="top:416px;">LADIES</div>
  <span class="price" style="left:509px;top:416px;">$77</span>
  <span class="price" style="left:597px;top:416px;">$88</span>
  <span class="price" style="left:686px;top:416px;">$99</span>
  <span class="price" style="left:775px;top:416px;">$110</span>

  <div class="row cat" style="top:443px;">FRINGE</div>
  <div class="row item lead" style="top:466px;">Trim</div><span class="price" style="left:509px;top:466px;">$25</span>
  <div class="row item lead" style="top:489px;">Restyle</div><span class="price" style="left:509px;top:489px;">$35</span>

  <div class="row cat" style="top:521px;">MENS</div>
  <div class="row item lead" style="top:545px;">Single blade clipper</div><span class="price" style="left:509px;top:545px;">$28</span>
  <div class="row item lead" style="top:567px;">Style cut</div><span class="price" style="left:509px;top:567px;">$42</span>

  <div class="row cat" style="top:607px;">CHILDREN</div>
  <div class="row item lead" style="top:630px;">10 and under</div><span class="price" style="left:509px;top:630px;">$24</span>
  <div class="row item lead" style="top:652px;">11-16 Male</div><span class="price" style="left:509px;top:652px;">$32</span>
  <div class="row item lead" style="top:675px;">11-16 Female</div><span class="price" style="left:509px;top:675px;">$48</span>
  <div class="row item lead" style="top:697px;">add a wash</div><span class="price" style="left:509px;top:697px;">$5</span>

  <div class="row cat lead" style="top:734px;">BLOWDRY</div>
  <span class="price" style="left:509px;top:734px;">$47</span>
  <span class="price" style="left:597px;top:734px;">$57</span>
  <span class="price" style="left:686px;top:734px;">$67</span>
  <span class="price" style="left:775px;top:734px;">$77</span>
  <div class="row item lead" style="top:757px;">Shampoo &amp; dry off</div><span class="price" style="left:509px;top:757px;">$25</span>

  <div class="foliage" role="img" aria-label="Tropical leaf illustration framing the photos"></div>
  <div class="photo-circle one" role="img" aria-label="Barber trimming a man's hair with comb and clippers"></div>
  <div class="photo-circle two" role="img" aria-label="Woman relaxing with a towel wrap during a head spa treatment"></div>

  <h2 class="section-title" style="left:58px;top:794px;"><span class="brace">{</span>TREATMENT<span class="brace">}</span></h2>
  <h2 class="section-title" style="left:455px;top:794px;"><span class="brace">{</span>UPSTYLE<span class="brace">}</span></h2>

  <div class="price-box" style="left:62px;">Deep treatment<div class="price-tag"><svg width="44" height="44"><use href="#badge"/></svg><b>35$</b></div></div>
  <div class="price-box" style="left:236px;">Head Spa ritual<div class="price-tag"><svg width="44" height="44"><use href="#badge"/></svg><b>65$</b></div></div>
  <div class="price-box" style="left:459px;padding-left:27px;">45 minutes<div class="price-tag"><svg width="44" height="44"><use href="#badge"/></svg><b>85$</b></div></div>
  <div class="price-box" style="left:631px;padding-left:26px;">60 minutes<div class="price-tag"><svg width="44" height="44"><use href="#badge"/></svg><b>120$</b></div></div>

  <div class="spa-photo" role="img" aria-label="Woman lying relaxed receiving a gentle scalp massage"></div>
  <p class="footnote">*Pricing is indicative of average products used and time taken for each service.<br>You will always receive a firm price after your consultation.</p>
</main>
</body>
</html>
```